Packaging design for a reclosable bag for our product

We have a logo, and we need to put it on packaging for our product and while we want the look to be simple, we want it to follow good design principles and also contain spaces for other product descriptions.

There will be 5 sizes at launch so I'd like 5 variations, one for each size.

I've included a few mockups of the type of bag that I made but they are all just rough ideas that I had.

I want the brand to look scientific and methodical and even a bit quirky, as in "wow this is a serious product but also a bit unusual."

```html
<!DOCTYPE html>
<html lang="en">
<head>
<meta charset="utf-8">
<title>NR4 Bias Lighting – Pouch Front</title>
<link rel="stylesheet" href="https://fonts.googleapis.com/css2?family=Michroma&family=Bebas+Neue&family=Arimo:wght@400;700&display=swap">
<style>
  :root {
    --backdrop: #c9c9c9;
    --pouch-black: #0c0c0c;
    --pouch-glow: #3a3a3a;
    --ink-white: #ffffff;
    --band-white: #f4f4f4;
    --icon-black: #111111;
  }
  * { box-sizing: border-box; margin: 0; padding: 0; }
  html, body {
    width: 1200px;
    height: 1200px;
    overflow: hidden;
    background: var(--backdrop);
  }
  .canvas {
    position: relative;
    width: 1200px;
    height: 1200px;
  }
  .pouch {
    position: absolute;
    left: 266px;
    top: 164px;
    width: 668px;
    height: 862px;
    background:
      radial-gradient(ellipse 300px 190px at 50% 306px, var(--pouch-glow) 0%, rgba(12,12,12,0) 100%),
      var(--pouch-black);
    overflow: hidden;
  }
  .hang-slot {
    position: absolute;
    left: 288px;
    top: 32px;
    width: 92px;
    height: 22px;
    border-radius: 11px;
    background: var(--backdrop);
  }
  .seal-line {
    position: absolute;
    left: 0;
    right: 0;
    top: 94px;
    height: 3px;
    background: #1d1d1d;
  }
  .brand-name {
    position: absolute;
    left: 0;
    right: 0;
    top: 226px;
    text-align: center;
    font-family: "Michroma", sans-serif;
    font-size: 150px;
    line-height: 200px;
    color: var(--ink-white);
    letter-spacing: -4px;
  }
  .product-line {
    position: absolute;
    left: 0;
    right: 0;
    top: 518px;
    text-align: center;
    font-family: "Michroma", sans-serif;
    font-size: 38px;
    line-height: 50px;
    color: var(--ink-white);
    letter-spacing: 1px;
  }
  .spec-band {
    position: absolute;
    left: 0;
    right: 0;
    top: 582px;
    height: 86px;
    background: var(--band-white);
    display: flex;
    align-items: center;
    justify-content: center;
    font-family: "Bebas Neue", sans-serif;
    font-size: 50px;
    color: var(--pouch-black);
    letter-spacing: 1px;
    padding-top: 4px;
  }
  .feature-panel {
    position: absolute;
    left: 86px;
    right: 86px;
    top: 694px;
    bottom: 0;
    background: var(--band-white);
    border-radius: 26px 26px 0 0;
    display: flex;
    justify-content: center;
    gap: 19px;
    padding-top: 30px;
  }
  .feature-badge {
    width: 76px;
    height: 78px;
    background: var(--icon-black);
    border-radius: 9px;
    display: flex;
    flex-direction: column;
    align-items: center;
    justify-content: flex-start;
    padding-top: 7px;
  }
  .feature-badge svg {
    width: 44px;
    height: 44px;
  }
  .feature-label {
    font-family: "Arimo", sans-serif;
    font-size: 13px;
    color: var(--ink-white);
    margin-top: 5px;
    white-space: nowrap;
  }
</style>
</head>
<body>
<main class="canvas">
  <section class="pouch">
    <div class="hang-slot"></div>
    <div class="seal-line"></div>

    <h1 class="brand-name">NR4</h1>
    <p class="product-line">BIAS LIGHTING</p>

    <div class="spec-band">6500K WHITE BIAS LIGHTING</div>

    <div class="feature-panel">
      <div class="feature-badge">
        <svg viewBox="0 0 44 44" aria-hidden="true">
          <g stroke="#fff" stroke-width="2" stroke-linecap="round">
            <line x1="22" y1="2" x2="22" y2="7"/>
            <line x1="22" y1="37" x2="22" y2="42"/>
            <line x1="2" y1="22" x2="7" y2="22"/>
            <line x1="37" y1="22" x2="42" y2="22"/>
            <line x1="8" y1="8" x2="11.5" y2="11.5"/>
            <line x1="32.5" y1="32.5" x2="36" y2="36"/>
            <line x1="36" y1="8" x2="32.5" y2="11.5"/>
            <line x1="11.5" y1="32.5" x2="8" y2="36"/>
          </g>
          <circle cx="22" cy="22" r="12" fill="#fff"/>
          <text x="22" y="25.5" text-anchor="middle" font-family="Arimo, sans-serif" font-weight="700" font-size="10" fill="#111">D65</text>
        </svg>
        <span class="feature-label">Simulated</span>
      </div>

      <div class="feature-badge">
        <svg viewBox="0 0 44 44" aria-hidden="true">
          <g fill="none" stroke="#fff" stroke-width="2">
            <circle cx="22" cy="20" r="16"/>
            <circle cx="22" cy="20" r="11"/>
            <circle cx="22" cy="20" r="6"/>
          </g>
          <circle cx="22" cy="20" r="2" fill="#fff"/>
          <line x1="6" y1="36" x2="40" y2="36" stroke="#fff" stroke-width="2" stroke-linecap="round"/>
        </svg>
        <span class="feature-label">Cable 5m</span>
      </div>

      <div class="feature-badge">
        <svg viewBox="0 0 44 44" aria-hidden="true">
          <circle cx="22" cy="22" r="17" fill="none" stroke="#fff" stroke-width="7" stroke-dasharray="4 2.2"/>
          <circle cx="22" cy="22" r="10" fill="#fff"/>
          <text x="22" y="25.5" text-anchor="middle" font-family="Arimo, sans-serif" font-weight="700" font-size="9" fill="#111">CRI</text>
        </svg>
        <span class="feature-label">90+</span>
      </div>

      <div class="feature-badge">
        <svg viewBox="0 0 44 44" aria-hidden="true">
          <rect x="12" y="3" width="20" height="38" rx="3" fill="#fff"/>
          <g fill="#111">
            <circle cx="17" cy="10" r="1.6"/><circle cx="22" cy="10" r="1.6"/><circle cx="27" cy="10" r="1.6"/>
            <circle cx="17" cy="15" r="1.6"/><circle cx="22" cy="15" r="1.6"/><circle cx="27" cy="15" r="1.6"/>
            <circle cx="17" cy="20" r="1.6"/><circle cx="22" cy="20" r="1.6"/><circle cx="27" cy="20" r="1.6"/>
            <circle cx="17" cy="25" r="1.6"/><circle cx="22" cy="25" r="1.6"/><circle cx="27" cy="25" r="1.6"/>
            <circle cx="17" cy="30" r="1.6"/><circle cx="22" cy="30" r="1.6"/><circle cx="27" cy="30" r="1.6"/>
          </g>
        </svg>
        <span class="feature-label">Controller</span>
      </div>
    </div>
  </section>
</main>
</body>
</html>
```